Nonprofit serving disconnected/homeless young adults (age 18-24) needs marketing

There are over 5 Million young adults in the U.S. who are neither working nor in school. Many of them 'aged out' of foster care or group homes, meaning the state doesn't provide care for them when they become an adult at age 18. These young adults have slipped through the cracks of society. Many are homeless, which often times leads to drug use, crime, young pregnancy, violence and prison. VANT is a nonprofit dedicated to providing young adults opportunities, resources and experiences to begin building a life they value. We do that via two channels: one our 6-month living program, where participants live expense-free. The requirement is they work full-time, and save at least 75% of their income. At the end of the 6 months, they have the money needed to get into their own place, along with starter furniture and household basics. All potential candidates for housing program come from the resource center VANTLink. It's where VANT offers immediate assistance to young adults, and in-turn we get to know them, and them us. This is essential to see if they're a fit for the housing program. The marketing piece is something young adults (and members of the community) receive. It should 1) be eye catching, maybe something like a path or a road with a phrase "have you chosen the path you're on?" "if given the chance, would you choose something different?" "this is your opportunity to get serious about what matters most to you" "want something different for you life, here's your chance" ...something to that effect. I want the graphics to be big, in your face, something eye catching.

After that, something that says: "here's how"
1. EVERYTHING IN LIFE STARTS WITH THE FIRST STEP: attend orientation on Tuesday if you haven't already
2. YOU WANT TO SOMETHING DIFFERENT FOR YOUR LIFE, YOU NEED TO DO SOMETHING DIFFERENT: our classes are it.
3. YOU WANT TO BE SUCCESSFUL? HANG OUT WITH LIKE-MINDED INDIVIDUALS: attend a volunteer day or fun activity.

(I uploaded our Logo and our new t-shirt design so you can get a look/feel of our current marketing. it should be somewhat modern, "cool" because we're talking to young adults and again - modern design with large graphics.)

Industry/Entity Type

School

```html
<!DOCTYPE html>
<html lang="en">
<head>
<meta charset="utf-8">
<title>VANT – Here's Your Chance</title>
<link rel="stylesheet" href="https://fonts.googleapis.com/css2?family=Lato:wght@400;700;900&display=swap">
<style>
  :root {
    --teal: #1a9b8a;
    --teal-light: #5cc4b2;
    --paper: #ffffff;
    --paper-shade: #e2e2e2;
    --ink: #2b2b2b;
    --white: #ffffff;
  }
  * { margin: 0; padding: 0; box-sizing: border-box; }
  html, body { width: 801px; height: 1200px; overflow: hidden; background: #ffffff; }
  .flyer {
    position: relative;
    width: 801px;
    height: 1200px;
    font-family: "Lato", Arial, sans-serif;
    background: linear-gradient(90deg, var(--paper-shade) 0%, var(--paper) 16%, var(--paper) 84%, var(--paper-shade) 100%);
    overflow: hidden;
  }
  .hero-photo {
    position: absolute;
    top: 0; left: 0;
    width: 801px; height: 540px;
    display: block;
  }
  .hero-headline {
    position: absolute;
    top: 50px; left: 0; width: 100%;
    text-align: center;
    color: var(--white);
    text-shadow: 0 2px 6px rgba(0,0,0,0.35);
  }
  .hero-kicker { font-size: 24px; font-weight: 400; letter-spacing: 0.2px; }
  .hero-title { font-size: 50px; font-weight: 700; letter-spacing: 0.5px; margin-top: 2px; line-height: 1.1; }

  .brand {
    position: absolute;
    top: 565px; left: 0; width: 100%;
    display: flex; justify-content: center; align-items: center; gap: 18px;
  }
  .brand-square { width: 64px; height: 64px; background: var(--teal); }
  .brand-name { font-size: 104px; font-weight: 900; color: var(--teal); letter-spacing: 6px; line-height: 1; }
  .brand-tagline {
    position: absolute; top: 688px; width: 100%;
    text-align: center; font-size: 11.5px; letter-spacing: 1.6px; color: var(--teal);
  }

  .intro {
    position: absolute; top: 730px; left: 70px; width: 661px;
    text-align: center; color: var(--ink);
  }
  .intro-lead { font-size: 20px; line-height: 1.3; margin-bottom: 4px; }
  .intro-body { font-size: 13px; line-height: 1.5; }

  .how {
    position: absolute; left: 0; bottom: 0;
    width: 100%; height: 262px;
    background: var(--teal);
    border-top: 6px solid var(--paper);
    box-shadow: 0 -6px 0 var(--teal-light);
    color: var(--white); text-align: center;
  }
  .how-title {
    display: flex; align-items: center; justify-content: center; gap: 14px;
    margin-top: 22px; font-size: 24px; font-weight: 700; letter-spacing: 0.5px;
  }
  .how-title::before, .how-title::after {
    content: ""; width: 140px; height: 2px; background: var(--white);
  }
  .how-steps { list-style: none; margin-top: 20px; padding: 0 120px; }
  .how-step { margin-bottom: 14px; }
  .step-head { font-size: 14px; font-weight: 700; line-height: 1.35; text-transform: uppercase; }
  .step-action { font-size: 13px; font-weight: 400; line-height: 1.35; text-transform: none; }
</style>
</head>
<body>
<main class="flyer">
  <svg class="hero-photo" viewBox="0 0 801 540" role="img" aria-label="Photograph of a straight open road running through a desert toward distant mountains under a blue sky">
    <defs>
      <linearGradient id="heroTones" x1="0" y1="0" x2="0" y2="1">
        <stop offset="0" stop-color="#1f4f86"/>
        <stop offset="0.3" stop-color="#8fb4cf"/>
        <stop offset="0.36" stop-color="#b99466"/>
        <stop offset="0.6" stop-color="#c98a3a"/>
        <stop offset="1" stop-color="#6b4a2a"/>
      </linearGradient>
    </defs>
    <path d="M0 0 H801 V522 Q400 432 0 522 Z" fill="url(#heroTones)"/>
    <path d="M0 522 Q400 432 801 522" fill="none" stroke="#1a9b8a" stroke-width="7"/>
  </svg>

  <header class="hero-headline">
    <p class="hero-kicker">Want Something Different for you Life</p>
    <h1 class="hero-title">HERE'S YOUR CHANCE</h1>
  </header>

  <div class="brand">
    <span class="brand-square"></span>
    <span class="brand-name">VANT</span>
  </div>
  <p class="brand-tagline">Growth. Purpose. Courage. Tomorrow.</p>

  <section class="intro">
    <p class="intro-lead">We do that via two channels: one our 6-month living program, where participants live expense-free.</p>
    <p class="intro-body">The requirement is they work full-time, and save at least 75% of their income. At the end of the 6 months, they have the money needed to get into their own place, along with starter furniture and household basics. All potential candidates for housing program come from the resource center VANTLink. It's where VANT offers immediate assistance to young adults, and in-turn we get to know them, and them us. This is essential to see if they're a fit for the housing program.</p>
  </section>

  <section class="how">
    <h2 class="how-title">HERE'S HOW</h2>
    <ol class="how-steps">
      <li class="how-step">
        <p class="step-head">1. Everything in life starts with the first step</p>
        <p class="step-action">attend orientation on Tuesday if you haven't already</p>
      </li>
      <li class="how-step">
        <p class="step-head">2. You want to something different for your life, you need to do something different: <span class="step-action">our classes are it.</span></p>
      </li>
      <li class="how-step">
        <p class="step-head">3. You want to be successful? Hang out with like-minded individuals</p>
        <p class="step-action">attend a volunteer day or fun activity.</p>
      </li>
    </ol>
  </section>
</main>
</body>
</html>
```